Waste management company seeks a new website design

We need a website design for an environmental services company called 'Rannamõisa Jäätmehooldus.' We manage waste collection and recycling for 100K+ households and businesses across Estonia. Please use logos and colors from attached CVI file. The design should be extensively usable for our self-service portal and have a mobile-first approach as it will be turned into an app in the future. The new website should highlight our commitment to sustainability and provide easy access to our services with a clean, modern design. UX inspiration from https://vorrix.eu/et-ee/

```html
<!DOCTYPE html>
<html lang="en">
<head>
<meta charset="utf-8">
<title>Rannamõisa Jäätmehooldus</title>
<link href="https://fonts.googleapis.com/css2?family=Outfit:wght@300;400;500;600;700;800&display=swap" rel="stylesheet">
<style>
:root{
  --lime:#cdd82b;
  --lime-dark:#b7c21f;
  --stone:#958b87;
  --ink:#1e1e1e;
  --muted:#5a5a5a;
  --white:#ffffff;
  --night:#060606;
}
*{margin:0;padding:0;box-sizing:border-box}
html,body{width:1200px;height:4827px;overflow:hidden;background:var(--white)}
body{font-family:"Outfit",sans-serif;color:var(--ink)}
.canvas{position:relative;width:1200px;height:4827px;overflow:hidden}
.abs{position:absolute}
.btn{position:absolute;display:flex;align-items:center;justify-content:center;gap:6px;background:var(--lime);color:var(--white);font-weight:600;font-size:13px;border-radius:20px;box-shadow:0 4px 10px rgba(160,170,20,.35)}
.btn .dot{width:11px;height:11px;border-radius:50%;background:var(--white);position:relative}
.btn .dot::after{content:"";position:absolute;left:3px;top:3px;border-left:5px solid var(--lime);border-top:2.5px solid transparent;border-bottom:2.5px solid transparent}
.section-title{position:absolute;left:0;width:1200px;text-align:center;font-weight:600;font-size:45px;letter-spacing:-.5px}
.rule{position:absolute;height:3px;width:72px;background:var(--lime);border-radius:2px}

/* header */
.topline{left:0;top:0;width:1200px;height:4px;background:#9b9290}
.brand{left:144px;top:21px;display:flex;align-items:center;gap:10px}
.brand-mark{width:40px;height:40px;border-radius:50%;background:var(--stone)}
.brand-name{font-size:19px;line-height:21px;font-weight:500;color:var(--stone)}
.nav{top:36px;font-size:13px;font-weight:500;color:#6b6360}
.nav.active{color:var(--lime)}
.signup{left:952px;top:26px;width:104px;height:40px;border-radius:20px;background:var(--stone);color:var(--white);font-size:14px;font-weight:600;display:flex;align-items:center;justify-content:center}

/* hero */
.hero-welcome{left:703px;top:306px;font-size:12px;font-weight:600;color:var(--lime)}
.hero-title{left:700px;top:322px;font-size:76px;font-weight:700;color:var(--white);line-height:1}
.hero-sub{left:703px;top:396px;font-size:36px;font-weight:600;color:var(--white);line-height:1}
.dots{left:705px;top:642px;display:flex;gap:6px;align-items:center}
.dots span{width:7px;height:7px;border-radius:50%;background:rgba(255,255,255,.6)}
.dots span.on{width:12px;height:12px;background:var(--white)}

/* about */
.about-text{left:622px;top:1026px;width:434px;font-size:12px;line-height:20px;color:var(--muted);text-align:justify}

/* services */
.service-card{position:absolute;width:437px;height:171px;background:var(--white);border-radius:22px}
.service-card h3{position:absolute;left:45px;top:32px;font-size:18px;font-weight:600}
.service-card p{position:absolute;left:45px;top:66px;width:250px;font-size:11px;line-height:20px;color:var(--muted);text-align:justify}
.service-card svg{position:absolute;left:318px;top:44px}

/* why */
.why-item{position:absolute;left:144px;width:454px;display:flex;gap:14px;align-items:flex-start}
.why-num{flex:none;width:34px;height:34px;border-radius:50%;background:var(--lime);color:var(--ink);font-size:12px;font-weight:600;display:flex;align-items:center;justify-content:center;margin-top:-2px}
.why-item p{font-size:12px;line-height:20px;color:var(--muted);text-align:justify}

/* how */
.step{position:absolute;width:190px;text-align:center;color:var(--white)}
.step-ring{position:absolute;width:142px;height:142px;border-radius:50%;border:3px solid var(--lime)}
.step-core{position:absolute;width:112px;height:112px;border-radius:50%;background:var(--white)}
.step-badge{position:absolute;width:40px;height:40px;border-radius:50%;background:var(--lime);color:var(--white);font-size:14px;font-weight:600;display:flex;align-items:center;justify-content:center}
.step h4{font-family:"Outfit",sans-serif;font-size:18px;font-weight:600;margin-bottom:6px}
.step p{font-size:12px;line-height:20px}

/* news */
.news-title{left:141px;top:3780px;font-size:45px;font-weight:600}
.news-card{position:absolute;width:287px;text-align:center}
.news-card .media{width:287px;height:193px;border-radius:8px}
.news-card h4{margin-top:28px;font-size:18px;font-weight:600;line-height:32px}
.news-card .date{margin-top:10px;font-size:12px;color:#8a8a8a;display:flex;justify-content:center;align-items:center;gap:6px;text-decoration:underline}

/* footer */
.foot-head{top:4522px;font-size:22px;font-weight:600;color:var(--white)}
.foot-list{list-style:none;top:4577px;font-size:12px;color:var(--white)}
.foot-list li{height:24px;display:flex;align-items:center;gap:14px}
.foot-list li::before{content:"»";font-size:13px}
.contact-list{list-style:none;left:872px;top:4577px;font-size:12px;color:var(--white)}
.contact-list li{display:flex;align-items:center;gap:16px;height:24px;margin-bottom:24px}
.social{top:4590px;width:34px;height:34px;border-radius:50%;border:1.5px solid var(--white)}
.copyright{left:0;top:4764px;width:1196px;text-align:center;font-size:12px;color:var(--white)}
</style>
</head>
<body>
<div class="canvas">

  <!-- header -->
  <div class="abs topline"></div>
  <div class="abs brand"><span class="brand-mark"></span><span class="brand-name">Rannamõisa<br>Jäätmehooldus</span></div>
  <span class="abs nav active" style="left:498px">Home</span>
  <span class="abs nav" style="left:568px">About</span>
  <span class="abs nav" style="left:639px">Services</span>
  <span class="abs nav" style="left:725px">Blog</span>
  <span class="abs nav" style="left:787px">Contact</span>
  <svg class="abs" style="left:889px;top:38px" width="14" height="14" viewBox="0 0 14 14"><circle cx="6" cy="6" r="4.5" fill="none" stroke="#8a817e" stroke-width="1.6"/><path d="M9.5 9.5 13 13" stroke="#8a817e" stroke-width="1.6"/></svg>
  <div class="signup">Sign Up</div>

  <!-- hero -->
  <svg class="abs" style="left:0;top:0" width="1200" height="820" viewBox="0 0 1200 820">
    <defs>
      <linearGradient id="heroSky" x1="0" y1="0" x2="1" y2="1">
        <stop offset="0" stop-color="#a99886"/>
        <stop offset=".45" stop-color="#d8c8b6"/>
        <stop offset="1" stop-color="#a08a72"/>
      </linearGradient>
    </defs>
    <path d="M0 545 Q600 1100 1200 500 L1200 540 Q600 1000 0 540 Z" fill="var(--lime)"/>
    <path role="img" aria-label="Photo of a woman with eyes closed enjoying the breeze beside a lake at sunset" d="M0 88 H1200 V540 Q600 1000 0 540 Z" fill="url(#heroSky)"/>
  </svg>
  <div class="abs hero-welcome">Welcome To</div>
  <div class="abs hero-title">Rannamõisa</div>
  <div class="abs hero-sub">Jäätmehooldus.</div>
  <div class="btn" style="left:705px;top:446px;width:127px;height:38px">Get Started</div>
  <div class="abs dots"><span class="on"></span><span></span><span></span><span></span></div>

  <!-- about -->
  <div class="abs" role="img" aria-label="Collage of a forest, an elderly woman and green leaves" style="left:118px;top:905px;width:430px;height:430px;border-radius:50%;background:radial-gradient(circle at 40% 40%,#8a7a5c,#5c4d36 55%,#6f7a2a)"></div>
  <div class="section-title" style="left:440px;width:800px;top:934px">About Us</div>
  <div class="rule" style="left:804px;top:1006px"></div>
  <p class="abs about-text">Lorem ipsum dolor sit amet, consectetur adipiscing elit, sed do eiusmod tempor incididunt ut labore et dolore magna aliqua. Ut enim ad minim veniam, quis nostrud exercitation ullamco laboris nisi ut aliquip ex ea commodo consequat. Duis aute irure dolor in reprehenderit in voluptate velit esse cillum dolore eu fugiat nulla pariatur. Excepteur sint occaecat cupidatat non proident, sunt in culpa qui officia deserunt mollit anim id est laborum. Lorem ipsum dolor sit amet, consectetur adipiscing elit, sed do eiusmod tempor incididunt ut labore et dolore magna aliqua. Ut enim ad minim veniam, quis nostrud exercitation ullamco laboris nisi ut aliquip ex ea commodo consequat. Duis aute irure dolor in reprehenderit in voluptate velit esse cillum dolore eu fugiat nulla pariatur. Excepteur sint occaecat cupidatat non proident, sunt in culpa qui officia deserunt mollit anim id est laborum.</p>
  <div class="btn" style="left:776px;top:1288px;width:128px;height:38px">Learn More <span class="dot"></span></div>

  <!-- services -->
  <svg class="abs" style="left:0;top:1400px" width="1200" height="790" viewBox="0 1400 1200 790">
    <defs>
      <linearGradient id="bogMist" x1="0" y1="0" x2="0" y2="1">
        <stop offset="0" stop-color="#7d6f68"/>
        <stop offset=".5" stop-color="#8e7a6a"/>
        <stop offset="1" stop-color="#6a5444"/>
      </linearGradient>
    </defs>
    <path d="M0 1690 Q600 1180 1200 1690 V1800 H0 Z" fill="var(--lime)"/>
    <path role="img" aria-label="Misty bog landscape with bare pines and a wooden boardwalk" d="M0 1720 Q600 1250 1200 1650 V2184 H0 Z" fill="url(#bogMist)"/>
  </svg>
  <div class="section-title" style="top:1577px;color:var(--white)">Our Services</div>
  <div class="rule" style="left:564px;top:1651px"></div>

  <div class="service-card" style="left:144px;top:1688px">
    <h3>Lorem ipsum dolor</h3>
    <p>Lorem ipsum dolor sit amet, consectetur adipiscing elit, sed do eiusmod tempor incididunt ut labore et dolore</p>
    <svg width="80" height="80" viewBox="0 0 80 80" fill="none" stroke="var(--lime)" stroke-width="2"><circle cx="40" cy="36" r="26"/><path d="M18 24c8 2 10 8 16 8s4 8 10 10M48 12c-2 6 4 10 10 10M24 58c4-6 2-10 8-12"/><path d="M12 54c4 10 10 16 18 18M68 54c-4 10-10 16-18 18"/></svg>
  </div>
  <div class="service-card" style="left:619px;top:1688px">
    <h3>Lorem ipsum dolor</h3>
    <p>Lorem ipsum dolor sit amet, consectetur adipiscing elit, sed do eiusmod tempor incididunt ut labore et dolore</p>
    <svg width="80" height="80" viewBox="0 0 80 80" fill="none" stroke="var(--lime)" stroke-width="2"><circle cx="36" cy="38" r="26"/><path d="M16 28c8 2 10 8 16 8s4 8 10 10M44 14c-2 6 4 10 10 10"/><path d="M58 46l12 4v10c0 6-6 10-12 12-6-2-12-6-12-12V50z"/></svg>
  </div>
  <div class="service-card" style="left:144px;top:1888px">
    <h3>Lorem ipsum dolor</h3>
    <p>Lorem ipsum dolor sit amet, consectetur adipiscing elit, sed do eiusmod tempor incididunt ut labore et dolore</p>
    <svg width="80" height="80" viewBox="0 0 80 80" fill="none" stroke="var(--lime)" stroke-width="2"><circle cx="40" cy="46" r="24"/><path d="M16 46h48M40 22v48M24 30c10 6 22 6 32 0M24 62c10-6 22-6 32 0"/><path d="M40 22c-8-4-12-12-8-18 6 2 10 10 8 18zM40 22c6-6 14-8 18-4-4 6-12 8-18 4z"/></svg>
  </div>
  <div class="service-card" style="left:619px;top:1888px">
    <h3>Lorem ipsum dolor</h3>
    <p>Lorem ipsum dolor sit amet, consectetur adipiscing elit, sed do eiusmod tempor incididunt ut labore et dolore</p>
    <svg width="80" height="80" viewBox="0 0 80 80" fill="none" stroke="var(--lime)" stroke-width="2"><path d="M30 18c10-8 24-4 28 6M62 36c4 14-4 26-16 28M22 62C12 54 10 40 16 30"/><path d="M34 46c-10 0-14-10-10-18 10 0 14 10 10 18zM54 44c6 6 4 18-6 20-4-8-2-16 6-20z"/></svg>
  </div>

  <!-- why choose us -->
  <div class="section-title" style="top:2280px">Why Choose Us</div>
  <div class="why-item" style="top:2405px"><span class="why-num">01</span><p>Lorem ipsum dolor sit amet, consectetur adipiscing elit, sed do eiusmod tempor incididunt ut labore et dolore magna aliqua.</p></div>
  <div class="why-item" style="top:2465px"><span class="why-num">02</span><p>Ut enim ad minim veniam, quis nostrud exercitation ullamco laboris nisi ut aliquip ex ea commodo consequat.</p></div>
  <div class="why-item" style="top:2527px"><span class="why-num">03</span><p>Duis aute irure dolor in reprehenderit in voluptate velit esse cillum dolore eu fugiat nulla pariatur.</p></div>
  <div class="why-item" style="top:2585px"><span class="why-num">04</span><p>Excepteur sint occaecat cupidatat non proident, sunt in culpa qui officia deserunt mollit anim id est laborum.</p></div>
  <div class="why-item" style="top:2646px"><span class="why-num">05</span><p>Lorem ipsum dolor sit amet, consectetur adipiscing elit, sed do eiusmod tempor incididunt ut labore et dolore magna aliqua.</p></div>
  <div class="btn" style="left:148px;top:2719px;width:128px;height:38px">Learn More <span class="dot"></span></div>
  <div class="abs" style="left:630px;top:2363px;width:438px;height:438px;border-radius:50%;border:3px solid var(--lime)"></div>
  <div class="abs" role="img" aria-label="Aerial view of a dense green forest with a recycling-shaped lake" style="left:643px;top:2376px;width:412px;height:412px;border-radius:50%;background:radial-gradient(circle at 50% 45%,#6c9a4a,#2f5e22 60%,#1f4216)"></div>

  <!-- how it works -->
  <svg class="abs" style="left:0;top:2900px" width="1200" height="780" viewBox="0 2900 1200 780">
    <defs>
      <linearGradient id="pineFog" x1="0" y1="0" x2="0" y2="1">
        <stop offset="0" stop-color="#6e6462"/>
        <stop offset=".45" stop-color="#8a817e"/>
        <stop offset=".7" stop-color="#3e3a32"/>
        <stop offset="1" stop-color="#5c4a38"/>
      </linearGradient>
    </defs>
    <path d="M0 3380 Q560 3960 1200 3400 V3420 Q600 3840 0 3400 Z" fill="var(--lime)"/>
    <path role="img" aria-label="Foggy pine forest beside an open autumn meadow" d="M0 2908 H1200 V3400 Q600 3840 0 3380 Z" fill="url(#pineFog)"/>
    <g fill="none" stroke="rgba(255,255,255,.75)" stroke-width="1.5" stroke-dasharray="3 4">
      <path d="M330 3168 Q370 3140 410 3172"/>
      <path d="M558 3168 Q598 3140 638 3172"/>
      <path d="M787 3168 Q827 3140 867 3172"/>
    </g>
  </svg>
  <div class="section-title" style="top:3018px;color:var(--white)">How It Works</div>
  <div class="rule" style="left:564px;top:3094px"></div>

  <div class="step-ring" style="left:186px;top:3154px"></div>
  <div class="step-core" style="left:201px;top:3169px"></div>
  <div class="step-badge" style="left:237px;top:3132px">01</div>
  <div class="step-ring" style="left:415px;top:3154px"></div>
  <div class="step-core" style="left:430px;top:3169px"></div>
  <div class="step-badge" style="left:466px;top:3132px">02</div>
  <div class="step-ring" style="left:643px;top:3154px"></div>
  <div class="step-core" style="left:658px;top:3169px"></div>
  <div class="step-badge" style="left:694px;top:3132px">03</div>
  <div class="step-ring" style="left:872px;top:3154px"></div>
  <div class="step-core" style="left:887px;top:3169px"></div>
  <div class="step-badge" style="left:923px;top:3132px">04</div>

  <svg class="abs" style="left:232px;top:3200px" width="50" height="50" viewBox="0 0 50 50" fill="none" stroke="var(--lime)" stroke-width="2"><path d="M6 26l10-10 8 4 8-6 12 12-10 10-8-4-8 6z"/><path d="M18 30l6 6M24 26l6 6M30 22l6 6"/></svg>
  <svg class="abs" style="left:461px;top:3200px" width="50" height="50" viewBox="0 0 50 50" fill="none" stroke="var(--lime)" stroke-width="2"><path d="M8 30l12-16 6 8M42 30L30 14l-6 8"/><path d="M14 34l10 8 12-10"/></svg>
  <svg class="abs" style="left:689px;top:3200px" width="50" height="50" viewBox="0 0 50 50" fill="none" stroke="var(--lime)" stroke-width="2"><rect x="8" y="10" width="34" height="24" rx="2"/><path d="M20 42h10M25 34v8"/><circle cx="25" cy="22" r="6"/><path d="M25 12v4M25 28v4M15 22h4M31 22h4"/></svg>
  <svg class="abs" style="left:918px;top:3200px" width="50" height="50" viewBox="0 0 50 50" fill="none" stroke="var(--lime)" stroke-width="2"><path d="M19 12l6-6 6 8M37 22l4 8-6 10h-8M13 40H9l-2-8 6-10"/><path d="M22 40l-4 -4 4-4M33 16l6 2-2 6M10 26l2-6 6 2"/></svg>

  <div class="step" style="left:162px;top:3306px"><h4>Lorem ipsumdo</h4><p>Lorem ipsum dolor sit amet, consectetur adipiscing elit, sed do eiusmod tempor</p></div>
  <div class="step" style="left:391px;top:3306px"><h4>Lorem ipsumdo</h4><p>Lorem ipsum dolor sit amet, consectetur adipiscing elit, sed do eiusmod tempor</p></div>
  <div class="step" style="left:619px;top:3306px"><h4>Lorem ipsumdo</h4><p>Lorem ipsum dolor sit amet, consectetur adipiscing elit, sed do eiusmod tempor</p></div>
  <div class="step" style="left:848px;top:3306px"><h4>Lorem ipsumdo</h4><p>Lorem ipsum dolor sit amet, consectetur adipiscing elit, sed do eiusmod tempor</p></div>

  <!-- news -->
  <div class="abs news-title">News and Stories</div>
  <div class="rule" style="left:144px;top:3847px"></div>
  <div class="btn" style="left:926px;top:3801px;width:128px;height:38px">View More <span class="dot"></span></div>

  <div class="news-card" style="left:144px;top:3885px">
    <div class="media" role="img" aria-label="Hand touching golden wheat at sunset" style="background:linear-gradient(160deg,#e8c37a,#9a7a3a 55%,#4a3b22)"></div>
    <h4>Lorem ipsum dolor sit amet,<br>consectetur</h4>
    <div class="date"><svg width="12" height="12" viewBox="0 0 12 12" fill="none" stroke="#8a8a8a"><rect x="1" y="2" width="10" height="9" rx="1"/><path d="M1 5h10M4 1v2M8 1v2"/></svg>Jan 20,2024</div>
  </div>
  <div class="news-card" style="left:456px;top:3885px">
    <div class="media" role="img" aria-label="Green recycling bin on a sunny meadow" style="background:linear-gradient(180deg,#a9c7dc,#dfe8e6 35%,#6f9a3a 55%,#3f6a22)"></div>
    <h4>Lorem ipsum dolor sit amet,<br>consectetur</h4>
    <div class="date"><svg width="12" height="12" viewBox="0 0 12 12" fill="none" stroke="#8a8a8a"><rect x="1" y="2" width="10" height="9" rx="1"/><path d="M1 5h10M4 1v2M8 1v2"/></svg>Jan 20,2024</div>
  </div>
  <div class="news-card" style="left:767px;top:3885px">
    <div class="media" role="img" aria-label="Hands holding a bunch of wildflowers" style="background:linear-gradient(150deg,#dfe6ea,#9eb08a 45%,#4d6a3a)"></div>
    <h4>Lorem ipsum dolor sit amet,<br>consectetur</h4>
    <div class="date"><svg width="12" height="12" viewBox="0 0 12 12" fill="none" stroke="#8a8a8a"><rect x="1" y="2" width="10" height="9" rx="1"/><path d="M1 5h10M4 1v2M8 1v2"/></svg>Jan 20,2024</div>
  </div>

  <!-- footer -->
  <svg class="abs" style="left:0;top:4150px" width="1200" height="677" viewBox="0 4150 1200 677">
    <path d="M0 4420 Q620 4160 1200 4380 V4827 H0 Z" fill="var(--lime)"/>
    <path d="M0 4560 Q700 4200 1200 4390 V4827 H0 Z" fill="var(--night)"/>
  </svg>
  <div class="abs brand" style="top:4530px"><span class="brand-mark"></span><span class="brand-name">Rannamõisa<br>Jäätmehooldus</span></div>
  <div class="abs social" style="left:142px"></div>
  <div class="abs social" style="left:183px"></div>
  <div class="abs social" style="left:223px"></div>

  <div class="abs foot-head" style="left:484px">Quick Links</div>
  <ul class="abs foot-list" style="left:486px"><li>Home</li><li>About Us</li><li>Services</li><li>Why Us?</li><li>Blog</li><li>Contact Us</li></ul>
  <div class="abs foot-head" style="left:675px">Company</div>
  <ul class="abs foot-list" style="left:677px"><li>Privacy policy</li><li>Terms &amp; Codition</li><li>Suport</li><li>Faq</li><li>Blog</li></ul>
  <div class="abs foot-head" style="left:870px">Contact Us</div>
  <ul class="contact-list abs">
    <li><svg width="12" height="14" viewBox="0 0 12 14"><path d="M6 0a5 5 0 0 1 5 5c0 4-5 9-5 9S1 9 1 5a5 5 0 0 1 5-5z" fill="var(--lime)"/><circle cx="6" cy="5" r="2" fill="var(--night)"/></svg>123, Lorem ipsum dolor sit</li>
    <li><svg width="12" height="12" viewBox="0 0 12 12"><path d="M2 0l3 3-1.5 2a7 7 0 0 0 3.5 3.5L9 7l3 3-2 2C5 12 0 7 0 2z" fill="var(--lime)"/></svg>+1 888 888 8888</li>
    <li><svg width="14" height="10" viewBox="0 0 14 10"><rect width="14" height="10" rx="1" fill="var(--lime)"/><path d="M1 1l6 5 6-5" fill="none" stroke="var(--night)" stroke-width="1.2"/></svg>info@companyname.com</li>
  </ul>
  <div class="abs copyright">© Copyrights 2024 | All Rights Reserved</div>
</div>
</body>
</html>
```